Create a Modern, On-Brand Zoom Background for Our LUMORA Webinar Team

Project Overview
We are hosting a Zoom webinar next month and want all team members to appear unified on-screen. We need a custom, branded Zoom background that incorporates our corporate identity while remaining clean, modern, and visually polished.
Design Requirements
File Type: Static image (no motion) optimized for Zoom virtual backgrounds
Orientation: 16:9 landscape
Main Logo: KALDRIN (primary)
Secondary Logo: LUMORA (supporting logo)
Design Style:
Clean, crisp, modern
Professional and easy on the eyes
Eye-catching but not busy or distracting
Bold enough to look strong on-camera but minimal enough to sit behind presenters
Color Palette: Use Kaldrin brand colors, LUMORA colors, or a subtle combination
Avoid: Clutter, heavy textures, distracting patterns, excessive gradients, motion effects
Preferred (Not Required)
Designs created in Canva are strongly preferred.
Designers who provide:
Editable Canva link
…will be prioritized, as this allows us to make future updates easily.
Deliverables
Final Zoom-ready JPG/PNG background
Source files (Canva preferred; AI/PSD acceptable)
Audience & Use Case
This background will be used by internal Kaldrin team members during a high-visibility webinar with physicians and clinical partners involved in the LUMORA study.

```html
<!DOCTYPE html>
<html lang="en">
<head>
<meta charset="utf-8">
<title>Kaldrin Webinar Background</title>
<link href="https://fonts.googleapis.com/css2?family=Oswald:wght@200;500&display=swap" rel="stylesheet">
<style>
  :root {
    --lime: #5fd014;
    --forest: #1f5a3a;
    --navy: #0a1f66;
    --navy-deep: #061650;
    --lab-blue: #1a3a8f;
    --white: #ffffff;
  }
  html, body {
    margin: 0;
    padding: 0;
    width: 1200px;
    height: 675px;
    overflow: hidden;
    background: var(--navy-deep);
  }
  .backdrop {
    position: relative;
    width: 1200px;
    height: 675px;
    overflow: hidden;
    background:
      radial-gradient(circle at 0 0, var(--lime) 0%, rgba(95,208,20,0.55) 14%, rgba(31,90,58,0.45) 32%, rgba(10,31,102,0) 58%),
      linear-gradient(160deg, var(--navy) 0%, #0b2070 45%, var(--navy-deep) 100%);
    font-family: "Oswald", sans-serif;
  }
  .lab-photo {
    position: absolute;
    top: 0;
    right: 0;
    width: 720px;
    height: 675px;
    background:
      radial-gradient(ellipse at 70% 45%, rgba(47,84,184,0.45) 0%, rgba(26,58,143,0.25) 45%, rgba(10,31,102,0) 75%),
      linear-gradient(90deg, rgba(26,58,143,0) 0%, rgba(26,58,143,0.35) 40%, rgba(16,36,110,0.5) 100%);
  }
  .primary-mark {
    position: absolute;
    left: 62px;
    top: 44px;
    margin: 0;
    font-weight: 200;
    font-size: 118px;
    line-height: 1;
    letter-spacing: 0;
    color: var(--white);
    transform: scaleX(0.78);
    transform-origin: left;
  }
  .study-mark {
    position: absolute;
    left: 62px;
    top: 576px;
    width: 205px;
    color: var(--white);
  }
  .study-name {
    display: block;
    font-weight: 500;
    font-size: 42px;
    line-height: 1;
    letter-spacing: -0.5px;
    transform: scaleX(0.86);
    transform-origin: left;
    white-space: nowrap;
  }
  .study-tagline {
    display: block;
    margin-top: 3px;
    padding-left: 30px;
    font-weight: 500;
    font-size: 5px;
    white-space: nowrap;
  }
</style>
</head>
<body>
  <main class="backdrop">
    <div class="lab-photo" role="img" aria-label="Softly blurred laboratory scene with glassware in deep blue tones"></div>

    <h1 class="primary-mark">KALDRIN</h1>

    <div class="study-mark">
      <span class="study-name">LUMORA U.S.</span>
      <span class="study-tagline">Solvia Disc NP Randomized, Sham-Controlled, Multi-Center, Double Blind Clinical Trial</span>
    </div>
  </main>
</body>
</html>
```